Design the Taste: Help Us Cook Up a Fresh Brochure for Our Wholesale Food Brand!

Overview:
We are looking for a fresh, eye-catching brochure design for our wholesale food company. The brochure can be up to 6 pages and should be visually appealing while clearly presenting our products and services.

Reference:
Please use the attached previous brochure as a guide for layout and style inspiration.

Content Requirements:
The brochure must highlight our key food groups:

Frozen Entrées
Pizzas
Frozen Meals and Party Size
Dry goods and Pasta
Gift Baskets
Delicacies and Sweets
Can do private label
Additional Highlights:

We deliver to our customers.
All products are fresh and locally made in Nashville, TN.

Design Goals:

Modern, appetizing, and professional design

Easy to read and navigate
Should NOT say Bruno's Tuscan Grocer and Trattoria but brand colors should resemble our parent company Brunos Tuscan Grocer and Trattoria
Strong visual focus on our products
Also mention we can brand with clients information
Incorporate brand colors and style from previous brochure

Phone: (615) 555-0172
https://brunossupplyandgoods.example/
use any pictures from this site: https://brunossupplyandgoods.example/

use circle logo for Bruno's Fine Tuscan Kitchen

Outstanding family dining and exquisite imported Italian delights.
Today, you’ll find our locally made dishes in markets, mini-marts, and corner stores across the city, making it easy for your clients to enjoy the taste of Bruno’s at home.

Alongside our prepared foods, we offer a curated selection of imported Italian goods, handcrafted gift baskets made in-house, and our signature marinara sauce, lovingly created from my Lulu’s treasured recipes.

Use only our pictures of pizza, pasta, dry pasta, marina sauce, canolis, frozen entrees, frozen dishes and meat dishes provided in breif and on website. Can also use pictures from our facebook and instra gram
https://www.facebook.com/brunossupply
https://www.instagram.com/brunos_supply/

Target Market(s)

Liquior stores, mini markets, gas stations and mini food places

Industry/Entity Type

Food

Font styles to use
Other font styles liked:
• Valadimir script and new times roman

Colors
59FF00
82FF00
B8FF75
E3FFCB
F4FFEA
EB3D1F
EC4F4E
F09395
F8D3D4
FCEDEE

Requirements
Must have
• Item sectiosn metnioned, logo, phone number and webaddress

```html
<!DOCTYPE html>
<html lang="en">
<head>
<meta charset="utf-8">
<title>Bruno's Fine Tuscan Kitchen – Wholesale Brochure</title>
<link rel="stylesheet" href="https://fonts.googleapis.com/css2?family=Great+Vibes&family=Montserrat:wght@400;500;600&display=swap">
<style>
:root{
  --ink:#0d0d0d;
  --red:#e0283a;
  --cream:#f4f1ec;
  --white:#ffffff;
  --text-dark:#1a1a1a;
  --icon:#555555;
  --script:'Great Vibes', cursive;
  --sans:'Montserrat', sans-serif;
}
*{box-sizing:border-box;margin:0;padding:0}
html,body{width:1200px;height:404px;overflow:hidden;background:var(--white)}
.sheet{position:relative;width:1200px;height:404px}
.panel{position:absolute;top:28px;width:268px;height:347px;overflow:hidden;background:var(--ink);font-family:var(--sans)}
.panel--cover{left:31px}
.panel--offer{left:321px;background:var(--cream)}
.panel--categories{left:611px;background:var(--cream)}
.panel--contact{left:901px}
.abs{position:absolute}
.script{font-family:var(--script);font-weight:400;color:var(--white);line-height:1;white-space:nowrap}
.accent{color:var(--red)}
.photo{position:absolute;border-radius:50%}

/* brand badge */
.badge{position:absolute;border-radius:50%;background:var(--white);border:3px solid var(--ink);box-shadow:0 0 0 2px var(--white);display:flex;align-items:center;justify-content:center}
.badge__name{font-family:var(--script);color:var(--ink);line-height:1}

/* footer */
.footer{position:absolute;left:0;right:0;bottom:0;height:25px;background:var(--ink);display:flex;align-items:center;justify-content:space-between;padding:0 12px}
.contact-item{display:flex;align-items:center;gap:6px;color:var(--white);font-size:6.3px}
.icon-ring{width:13px;height:13px;border-radius:50%;border:1px solid var(--red);display:flex;align-items:center;justify-content:center;flex:none}
.icon-ring svg{width:6px;height:6px}

/* cover */
.cover__title{left:17px;top:20px;font-size:17px}
.cover__tagline{left:0;right:0;top:245px;text-align:center;font-size:15px;line-height:1.5}
.cover__sub{left:0;right:0;top:293px;text-align:center;color:var(--white);font-size:7px}
.cover .footer{background:transparent}

/* offer */
.offer__title{right:24px;top:44px;font-size:19px}
.offer-card{position:absolute;width:112px;height:50px;background:var(--white);border-radius:25px;box-shadow:0 1px 3px rgba(0,0,0,.08)}
.offer-card__photo{position:absolute;left:0;top:0;width:50px;height:50px;border-radius:50%;border:2px solid var(--white);box-shadow:0 1px 3px rgba(0,0,0,.25)}
.offer-card__script{position:absolute;left:60px;top:11px;font-family:var(--script);font-size:11.5px;color:var(--text-dark);line-height:1;white-space:nowrap}
.offer-card__label{position:absolute;left:60px;top:29px;font-size:6.3px;font-weight:500;color:var(--red);line-height:1.45}

/* categories */
.cat__title{right:32px;font-size:17px;text-align:right}
.cat{position:absolute;width:100px}
.cat__icon{position:absolute;left:-21px;top:0;width:12px;height:12px}
.cat__name{font-family:var(--script);font-size:12px;color:var(--red);line-height:1;white-space:nowrap}
.cat__name--long{font-size:10.5px}
.cat__desc{margin-top:6px;font-size:6.3px;line-height:1.8;color:var(--text-dark)}

/* contact */
.contact__lead{right:38px;top:26px;font-size:18px}
.contact__motto{right:38px;top:56px;font-size:19px}
.contact__line{right:38px;top:90px;color:var(--white);font-size:7px}
.contact__row{right:38px;display:flex;align-items:center;gap:10px;color:var(--white);font-size:6.8px}
</style>
</head>
<body>
<main class="sheet">

  <!-- Panel 1: cover -->
  <section class="panel panel--cover">
    <svg class="abs" style="left:0;top:0" width="268" height="235" viewBox="0 0 268 235" role="img" aria-label="Photo of a whole pepperoni pizza with a slice being lifted, on a warm glowing backdrop">
      <defs>
        <radialGradient id="cover-glow" cx="0.55" cy="0.4" r="0.85">
          <stop offset="0" stop-color="#b8621c"/>
          <stop offset="0.5" stop-color="#6e2c0b"/>
          <stop offset="1" stop-color="#1e0a04"/>
        </radialGradient>
        <radialGradient id="pizza-top" cx="0.5" cy="0.45" r="0.6">
          <stop offset="0" stop-color="#f0b24a"/>
          <stop offset="0.6" stop-color="#e08a36"/>
          <stop offset="0.85" stop-color="#c7552a"/>
          <stop offset="1" stop-color="#d99a58"/>
        </radialGradient>
      </defs>
      <path d="M0 0H268V180C230 176 200 200 160 212C110 228 60 208 0 218Z" fill="url(#cover-glow)"/>
      <ellipse cx="150" cy="120" rx="102" ry="46" transform="rotate(-12 150 120)" fill="url(#pizza-top)"/>
    </svg>
    <h1 class="abs script cover__title">Bruno’s Fine Tuscan Kitchen</h1>
    <div class="badge" style="left:144px;top:163px;width:60px;height:60px"><span class="badge__name" style="font-size:17px">Bruno’s</span></div>
    <p class="abs script cover__tagline">Outstanding Family Dining and <span class="accent">Exquisite</span><br><span class="accent">Imported Italian Delights.</span></p>
    <p class="abs cover__sub">Locally made in Nashville. Delivered to you</p>
    <footer class="footer">
      <span class="contact-item"><span class="icon-ring"><svg viewBox="0 0 10 10"><path d="M2 1l2 2-1 1.2c.6 1.3 1.5 2.2 2.8 2.8L7 6l2 2-1.3 1.3C4.5 9 1 5.5.7 2.3Z" fill="#fff"/></svg></span>(615) 555-0172</span>
      <span class="contact-item"><span class="icon-ring"><svg viewBox="0 0 10 10"><circle cx="5" cy="5" r="4" fill="none" stroke="#fff"/><path d="M1 5h8M5 1c-2 2.5-2 5.5 0 8M5 1c2 2.5 2 5.5 0 8" fill="none" stroke="#fff" stroke-width=".7"/></svg></span>brunossupplyandgoods.example</span>
    </footer>
  </section>

  <!-- Panel 2: what we offer -->
  <section class="panel panel--offer">
    <svg class="abs" style="left:0;top:0" width="268" height="110" viewBox="0 0 268 110" aria-hidden="true">
      <path d="M0 0H268V98C230 115 190 98 150 82C110 66 70 100 30 100C18 100 8 98 0 96Z" fill="var(--ink)"/>
    </svg>
    <div class="photo" role="img" aria-label="Photo of a vegetable pizza" style="left:-12px;top:42px;width:48px;height:58px;background:radial-gradient(circle at 55% 50%,#d8432e 0,#c85a34 45%,#7a9a3a 62%,#e6b878 80%,#d79a5a 100%)"></div>
    <h2 class="abs script offer__title">What We <span class="accent">Offer</span></h2>
    <div class="badge" style="left:55px;top:41px;width:64px;height:64px"><span class="badge__name" style="font-size:18px">Bruno’s</span></div>

    <div class="offer-card" style="left:15px;top:121px"><div class="offer-card__photo" role="img" aria-label="Photo of a pepperoni pizza" style="background:radial-gradient(circle at 45% 45%,#d4552c 0,#b8321c 45%,#d9823a 72%,#9a4a22 100%)"></div><span class="offer-card__script">Handmade</span><span class="offer-card__label">PIZZAS</span></div>
    <div class="offer-card" style="left:140px;top:121px"><div class="offer-card__photo" role="img" aria-label="Photo of a penne pasta dish" style="background:radial-gradient(circle at 50% 50%,#d83a2c 0,#eaa860 40%,#f3e4cc 68%,#b9c4cc 100%)"></div><span class="offer-card__script">Handmade</span><span class="offer-card__label">PASTAS</span></div>
    <div class="offer-card" style="left:15px;top:187px"><div class="offer-card__photo" role="img" aria-label="Photo of assorted fresh cheeses" style="background:radial-gradient(circle at 60% 55%,#f7f2e4 0,#e8d49a 40%,#cbbf9c 70%,#9e978a 100%)"></div><span class="offer-card__script">Fresh</span><span class="offer-card__label">CHEESES</span></div>
    <div class="offer-card" style="left:140px;top:187px"><div class="offer-card__photo" role="img" aria-label="Photo of a frozen dinner bowl with greens" style="background:radial-gradient(circle at 50% 45%,#c9a078 0,#7d9a4e 35%,#3c4a34 70%,#6b6d70 100%)"></div><span class="offer-card__script">Dinners</span><span class="offer-card__label">FROZEN</span></div>
    <div class="offer-card" style="left:15px;top:253px"><div class="offer-card__photo" role="img" aria-label="Photo of marinated vegetables in a bowl" style="background:radial-gradient(circle at 45% 40%,#b84a1e 0,#8a3a18 35%,#7aa03a 65%,#22201e 100%)"></div><span class="offer-card__script">Fresh</span><span class="offer-card__label">MARINATED<br>VEGGIES</span></div>
    <div class="offer-card" style="left:140px;top:253px"><div class="offer-card__photo" role="img" aria-label="Photo of sliced meat with glazed vegetables" style="background:radial-gradient(circle at 55% 55%,#9a2e26 0,#c8642a 35%,#4a2a1c 65%,#262220 100%)"></div><span class="offer-card__script">Bruno’s</span><span class="offer-card__label">SAUSES &amp;<br>GLAZES</span></div>
    <div class="photo" role="img" aria-label="Photo of a pasta salad" style="left:228px;top:283px;width:50px;height:50px;background:radial-gradient(circle,#e9c060 0,#d9a040 35%,#6f9a3a 60%,#f2ece2 82%)"></div>

    <footer class="footer">
      <span class="contact-item"><span class="icon-ring"><svg viewBox="0 0 10 10"><path d="M2 1l2 2-1 1.2c.6 1.3 1.5 2.2 2.8 2.8L7 6l2 2-1.3 1.3C4.5 9 1 5.5.7 2.3Z" fill="#fff"/></svg></span>(615) 555-0172</span>
      <span class="contact-item"><span class="icon-ring"><svg viewBox="0 0 10 10"><circle cx="5" cy="5" r="4" fill="none" stroke="#fff"/><path d="M1 5h8M5 1c-2 2.5-2 5.5 0 8M5 1c2 2.5 2 5.5 0 8" fill="none" stroke="#fff" stroke-width=".7"/></svg></span>brunossupplyandgoods.example</span>
    </footer>
  </section>

  <!-- Panel 3: categories -->
  <section class="panel panel--categories">
    <svg class="abs" style="left:0;top:0" width="268" height="120" viewBox="0 0 268 120" aria-hidden="true">
      <path d="M0 0H268V110C235 112 205 100 170 88C135 76 110 70 70 70C40 70 20 70 0 68Z" fill="var(--ink)"/>
    </svg>
    <div class="photo" role="img" aria-label="Photo of a vegetable pizza" style="left:236px;top:62px;width:52px;height:52px;background:radial-gradient(circle at 50% 50%,#d8432e 0,#c85a34 45%,#7a9a3a 62%,#e6b878 80%,#d79a5a 100%)"></div>
    <h2 class="abs script cat__title" style="top:22px">Our <span class="accent">Specialty</span> Food</h2>
    <h2 class="abs script cat__title" style="top:48px;right:30px">Categories</h2>
    <div class="badge" style="left:54px;top:41px;width:64px;height:64px"><span class="badge__name" style="font-size:18px">Bruno’s</span></div>

    <div class="cat" style="left:33px;top:114px"><svg class="cat__icon" viewBox="0 0 12 12"><rect x="1.5" y="2" width="9" height="8" rx="1" fill="none" stroke="var(--icon)" stroke-width=".8"/></svg><div class="cat__name">Frozen Entrées</div><p class="cat__desc">Classic Italian favorites ready to<br>heat and serve</p></div>
    <div class="cat" style="left:173px;top:114px"><svg class="cat__icon" viewBox="0 0 12 12"><circle cx="6" cy="6" r="4.5" fill="none" stroke="var(--icon)" stroke-width=".8"/></svg><div class="cat__name">Pizzas</div><p class="cat__desc">Handcrafted, artisan-style<br>pizzas</p></div>
    <div class="cat" style="left:33px;top:170px"><svg class="cat__icon" viewBox="0 0 12 12"><rect x="1.5" y="3" width="9" height="7" rx="1" fill="none" stroke="var(--icon)" stroke-width=".8"/></svg><div class="cat__name cat__name--long">Frozen Meals &amp; Party Size</div><p class="cat__desc">Perfect for gatherings and<br>events</p></div>
    <div class="cat" style="left:173px;top:170px"><svg class="cat__icon" viewBox="0 0 12 12"><rect x="3" y="1.5" width="6" height="9" rx="1" fill="none" stroke="var(--icon)" stroke-width=".8"/></svg><div class="cat__name">Dry Goods &amp; Pasta</div><p class="cat__desc">Premium imported Italian<br>essentials</p></div>
    <div class="cat" style="left:33px;top:225px"><svg class="cat__icon" viewBox="0 0 12 12"><path d="M2 5h8l-1 5H3Z" fill="none" stroke="var(--icon)" stroke-width=".8"/></svg><div class="cat__name">Gift Baskets</div><p class="cat__desc">Custom curated for any<br>occasion</p></div>
    <div class="cat" style="left:173px;top:225px"><svg class="cat__icon" viewBox="0 0 12 12"><rect x="1.5" y="4" width="9" height="6" fill="none" stroke="var(--icon)" stroke-width=".8"/></svg><div class="cat__name">Delicacies &amp; Sweets</div><p class="cat__desc">Indulgent desserts and<br>treats</p></div>
    <div class="cat" style="left:110px;top:279px"><svg class="cat__icon" viewBox="0 0 12 12"><path d="M3 4h6l1 7H2Z" fill="none" stroke="var(--icon)" stroke-width=".8"/></svg><div class="cat__name">Private Label Options</div><p class="cat__desc" style="margin-top:4px">Your brand, our quality</p></div>
    <div class="photo" role="img" aria-label="Photo of a pasta salad" style="left:-14px;top:266px;width:50px;height:60px;background:radial-gradient(circle,#e9c060 0,#d9a040 35%,#6f9a3a 60%,#f2ece2 82%)"></div>

    <footer class="footer">
      <span class="contact-item"><span class="icon-ring"><svg viewBox="0 0 10 10"><path d="M2 1l2 2-1 1.2c.6 1.3 1.5 2.2 2.8 2.8L7 6l2 2-1.3 1.3C4.5 9 1 5.5.7 2.3Z" fill="#fff"/></svg></span>(615) 555-0172</span>
      <span class="contact-item"><span class="icon-ring"><svg viewBox="0 0 10 10"><circle cx="5" cy="5" r="4" fill="none" stroke="#fff"/><path d="M1 5h8M5 1c-2 2.5-2 5.5 0 8M5 1c2 2.5 2 5.5 0 8" fill="none" stroke="#fff" stroke-width=".7"/></svg></span>brunossupplyandgoods.example</span>
    </footer>
  </section>

  <!-- Panel 4: contact -->
  <section class="panel panel--contact">
    <svg class="abs" style="left:0;top:0" width="268" height="347" viewBox="0 0 268 347" role="img" aria-label="Photo of tortellini in tomato cream sauce with spinach and parmesan">
      <defs>
        <radialGradient id="tortellini" cx="0.55" cy="0.55" r="0.75">
          <stop offset="0" stop-color="#e3a050"/>
          <stop offset="0.45" stop-color="#c86a32"/>
          <stop offset="0.8" stop-color="#a3401e"/>
          <stop offset="1" stop-color="#5a3a22"/>
        </radialGradient>
      </defs>
      <path d="M0 155C40 180 80 215 130 220C180 225 230 220 268 235V347H0Z" fill="url(#tortellini)"/>
    </svg>
    <h2 class="abs script contact__lead">Get In Touch</h2>
    <h2 class="abs script contact__motto">Authentic. <span class="accent">Local.</span> Delivered.</h2>
    <p class="abs contact__line">Let us bring the taste of Italy to your customers.</p>
    <div class="abs contact__row" style="top:113px">(615) 555-0172<span class="icon-ring"><svg viewBox="0 0 10 10"><path d="M2 1l2 2-1 1.2c.6 1.3 1.5 2.2 2.8 2.8L7 6l2 2-1.3 1.3C4.5 9 1 5.5.7 2.3Z" fill="#fff"/></svg></span></div>
    <div class="abs contact__row" style="top:137px">brunossupplyandgoods.example<span class="icon-ring"><svg viewBox="0 0 10 10"><circle cx="5" cy="5" r="4" fill="none" stroke="#fff"/><path d="M1 5h8M5 1c-2 2.5-2 5.5 0 8M5 1c2 2.5 2 5.5 0 8" fill="none" stroke="#fff" stroke-width=".7"/></svg></span></div>
    <div class="badge" style="left:50px;top:167px;width:76px;height:76px"><span class="badge__name" style="font-size:21px">Bruno’s</span></div>
  </section>

</main>
</body>
</html>
```